BUSINESS CARD - HALVERDINE RURAL SERVICES

I would like to create a business card for my fertilizer spreading business. I would like to incorporate my existing logo and also a description of the services offered. The business card will be given to farmers so must be kept simple but effective. It will also be left in stores so much also be eye catching in order to stand out from other cards.

Target Market(s)

FARMERS

Requirements
Must have
• FRONT OF CARD = EXISTING LOGO + "CUSTOMISED SPREADING" below the logo

REAR Of CARD = SERVICES OFFERED AND CONTACT DETAILS

- Bulk fertilizer including Lime, Gypsum, Manure & Compost
- Granular fertilizer including Single Super, Urea, Gran-am, & Custom Blends
- Modern equipment - Autosteer & Variable Rate Capable
- Friendly & Reliable Service
- Contact Gus: 0471 502 318
Nice to have
• utilize same color scheme as existing logo

```html
<!DOCTYPE html>
<html lang="en">
<head>
<meta charset="utf-8">
<title>Halverdine Rural Services – Business Card</title>
<link href="https://fonts.googleapis.com/css2?family=Montserrat:wght@500;600&family=Arimo:wght@400&display=swap" rel="stylesheet">
<style>
  :root {
    --backdrop: #adb5bf;
    --card: #ffffff;
    --charcoal: #58585a;
    --orange: #f7941d;
    --text: #4a4a4c;
  }
  html, body {
    margin: 0;
    width: 1200px;
    height: 1200px;
    overflow: hidden;
    background: var(--backdrop);
  }
  .canvas {
    position: relative;
    width: 1200px;
    height: 1200px;
  }
  .card {
    position: absolute;
    left: 264px;
    width: 672px;
    height: 402px;
    background: var(--card);
    overflow: hidden;
  }
  .card--services { top: 172px; }
  .card--brand { top: 614px; }

  .brand-mark {
    position: absolute;
    display: flex;
    flex-direction: column;
    align-items: center;
    text-align: center;
  }
  .brand-mark__circle {
    border-radius: 50%;
    background: var(--charcoal);
  }
  .brand-mark__name {
    font-family: "Montserrat", sans-serif;
    font-weight: 600;
    color: var(--charcoal);
    line-height: 1.1;
  }

  .card--services .brand-mark {
    left: 0; right: 0; top: 24px;
  }
  .card--services .brand-mark__circle {
    width: 88px; height: 88px;
  }
  .card--services .brand-mark__name {
    margin-top: 10px;
    font-size: 24px;
  }

  .services-list {
    position: absolute;
    left: 0; right: 0; top: 186px;
    margin: 0; padding: 0;
    list-style: none;
    text-align: center;
    font-family: "Arimo", sans-serif;
    font-size: 15.5px;
    line-height: 22.5px;
    color: var(--text);
  }

  .contact-band {
    position: absolute;
    left: 0; right: 0; top: 317px;
    height: 39px;
    background: var(--charcoal);
    font-family: "Montserrat", sans-serif;
    font-weight: 500;
    font-size: 18px;
    color: #ffffff;
  }
  .contact-band__label {
    position: absolute;
    right: 400px; top: 0;
    line-height: 39px;
  }
  .contact-band__number {
    position: absolute;
    left: 395px; top: 0;
    line-height: 39px;
  }
  .contact-band__icon {
    position: absolute;
    left: 306px; top: -12px;
    width: 60px; height: 60px;
  }

  .card__sweep {
    position: absolute;
    inset: 0;
    width: 672px;
    height: 402px;
  }
  .card--brand .brand-mark {
    left: 230px; right: 0; top: 82px;
  }
  .card--brand .brand-mark__circle {
    width: 150px; height: 150px;
  }
  .card--brand .brand-mark__name {
    margin-top: 16px;
    font-size: 36px;
  }
</style>
</head>
<body>
<div class="canvas">

  <section class="card card--services">
    <div class="brand-mark">
      <div class="brand-mark__circle"></div>
      <div class="brand-mark__name">Halverdine Rural Services</div>
    </div>

    <ul class="services-list">
      <li>Bulk fertilizer including Lime, Gypsum, Manure &amp; Compos</li>
      <li>Granular fertilizer including Single Super, Urea, Gran-am, &amp; Custom Blends</li>
      <li>Modern equipment - Autosteer &amp; Variable Rate Capable</li>
      <li>Friendly &amp; Reliable Service</li>
    </ul>

    <div class="contact-band">
      <span class="contact-band__label">Contact Gus</span>
      <svg class="contact-band__icon" viewBox="0 0 60 60" aria-hidden="true">
        <circle cx="30" cy="30" r="28" fill="#58585a"/>
        <circle cx="30" cy="30" r="23" fill="#f7941d"/>
        <path d="M22 19c1.5-1 3-.8 3.8.6l2.2 3.8c.6 1.1.3 2.3-.7 3l-1.6 1.1c1.1 2.8 3.4 5.3 6.4 6.6l1.2-1.5c.8-1 2.1-1.2 3.1-.5l3.6 2.4c1.3.9 1.4 2.4.4 3.7l-1.4 1.6c-1.3 1.4-3.4 1.8-5.3 1C26.6 38.6 20.4 32 18.5 25c-.5-2 .1-3.9 1.6-5z" fill="#ffffff"/>
      </svg>
      <span class="contact-band__number">0471 502 318</span>
    </div>
  </section>

  <section class="card card--brand">
    <svg class="card__sweep" viewBox="0 0 672 402" aria-hidden="true">
      <rect width="672" height="402" fill="#58585a"/>
      <path d="M238 0 C 46 90, 44 320, 180 402 L672 402 L672 0 Z" fill="#f7941d"/>
      <path d="M254 0 C 72 90, 70 320, 196 402 L672 402 L672 0 Z" fill="#ffffff"/>
    </svg>
    <div class="brand-mark">
      <div class="brand-mark__circle"></div>
      <div class="brand-mark__name">Halverdine Rural<br>Services</div>
    </div>
  </section>

</div>
</body>
</html>
```